STI/STD Medical Clinic- Wellspring Crest Partners, Inc Website

We are a STI clinic in florida looking for a website. We want to be professional but also playful. We want a buildout similar to the website listed below as our clinic is very similar to theirs.

This is a great example of a clinic doing similar stuff as us. We obviously do not want their color scheme but their format and buildout work. Please see our logo attached for color schemes etc.

https://bluefernclinicmiami.org

Industry/Entity Type

Medical

Coding

Coded - Design and coding required

Number of Pages Required

5+ page

Font styles to use
Sans Serif

```html
<!DOCTYPE html>
<html lang="en">
<head>
<meta charset="utf-8">
<title>Wellspring Crest Partners – STI/STD Medical Clinic</title>
<link rel="stylesheet" href="https://fonts.googleapis.com/css2?family=Josefin+Sans:wght@400;600;700&family=Montserrat:wght@400;500;600&display=swap">
<style>
:root{
  --ink:#1d1d24;
  --muted:#7a7a84;
  --orange:#f0602e;
  --blue:#2f5fbf;
  --violet:#6a3fb0;
  --pill:#5a2ea6;
  --grey-bg:#f4f4f7;
  --white:#ffffff;
  --line:#d9d9e0;
}
*{margin:0;padding:0;box-sizing:border-box}
html,body{width:1200px;height:4762px;overflow:hidden}
body{position:relative;font-family:"Montserrat",sans-serif;color:var(--ink);background:var(--white)}
.abs{position:absolute}
.heading{font-family:"Josefin Sans",sans-serif;font-weight:600;letter-spacing:1px;text-transform:uppercase}
.btn-outline{position:absolute;display:flex;align-items:center;justify-content:center;border:1.5px solid #444;border-radius:30px;font-size:17px;font-weight:500;letter-spacing:.5px;text-transform:uppercase;color:var(--ink)}
.body-copy{font-size:15px;line-height:28.5px;color:var(--muted)}

/* hero */
.hero{top:0;left:0;width:1200px;height:751px;background:linear-gradient(180deg,#5a4fe0 0%,#8a63d8 30%,#e28a8a 62%,#f3a465 78%,#9a5a4a 100%)}
.topbar{top:14px;right:113px;display:flex;align-items:center;gap:14px;font-size:14px;color:#fff}
.topbar .sep{opacity:.7}
.donate{border:1.5px solid #fff;border-radius:20px;padding:8px 14px;font-weight:600;font-size:14px}
.nav{top:59px;left:111px;width:976px;height:113px;background:#fff;border-radius:12px;display:flex;align-items:center;justify-content:space-between;padding:0 40px 0 22px}
.brand{display:flex;align-items:center;gap:12px;font-family:"Josefin Sans",sans-serif;font-weight:700;font-size:26px;color:var(--violet);line-height:1}
.brand .dot{width:40px;height:40px;border-radius:50%;background:var(--violet)}
.menu{display:flex;gap:22px;font-size:16px;font-weight:500;text-transform:uppercase}
.menu .active{color:var(--orange)}
.hero-title{top:276px;left:111px;font-size:54px;color:#fff}
.hero-sub{top:348px;left:111px;font-family:"Josefin Sans",sans-serif;font-size:37px;color:#fff;letter-spacing:1.5px}
.hero-btn{top:420px;left:111px;width:279px;height:72px;background:#fff;border-radius:40px;display:flex;align-items:center;justify-content:center;font-size:17px;font-weight:500;letter-spacing:.5px}

/* welcome */
.welcome-art{top:795px;left:37px;width:573px;height:583px;border-radius:50%;background:radial-gradient(circle,#f2d8e4 0%,#e6e0f5 45%,#ffffff 75%)}
.welcome-title{top:838px;left:645px;font-size:40px;line-height:53px}
.welcome-copy{top:1015px;left:645px;width:444px}

/* treatments */
.treatments{top:1420px;left:0;width:1200px;height:693px;background:var(--grey-bg)}
.section-title{left:0;width:1200px;text-align:center;font-size:40px}
.treat{position:absolute;top:1586px;width:232px;text-align:center}
.treat svg{display:block;margin:0 auto}
.treat h3{margin-top:20px;font-family:"Josefin Sans",sans-serif;font-weight:600;font-size:21px;letter-spacing:.8px}
.treat p{margin-top:16px;font-size:14.5px;line-height:25px;color:var(--muted)}

/* std */
.std{top:2113px;left:0;width:1200px;height:623px;background:linear-gradient(120deg,#4a58c9 0%,#6a4cc0 55%,#8c4cb8 100%)}
.std-title{top:2184px;left:111px;font-size:40px;line-height:53px;color:#fff}
.std-copy{top:2365px;left:111px;width:456px;color:#eef}
.pill{position:absolute;left:695px;width:392px;height:78px;border-radius:40px;background:var(--pill);color:#fff;display:flex;align-items:center;justify-content:center;font-size:22px;font-weight:600}
.btn-light{border-color:#fff;color:#fff}

/* member */
.member-photo{top:2890px;left:266px;width:668px;height:386px;background:linear-gradient(180deg,#eef3f8 0%,#b9d7ec 55%,#8fc1e3 100%)}
.member-text{top:3313px;left:0;width:1200px;text-align:center;font-size:16px}

/* appointment */
.appt{top:3489px;left:0;width:1200px;height:825px;background:linear-gradient(100deg,#c1548f 0%,#d86078 50%,#ec7158 100%)}
.appt-title{top:3550px;font-size:40px;color:#fff}
.appt-sub{top:3608px;left:0;width:1200px;text-align:center;font-size:15px;color:#ffe3ea}
.label{position:absolute;font-size:15px;color:#fff}
.field{position:absolute;background:#fff;border:1px solid #e8d0d8}
.check{position:absolute;top:3905px;display:flex;align-items:center;gap:8px;font-size:15px;color:#fff}
.check span.box{width:14px;height:14px;border:1.5px solid #fff;border-radius:2px}

/* footer */
.footer-copy{top:4518px;left:111px;width:360px;font-size:15px;line-height:27px;color:#555}
.foot-head{position:absolute;top:4383px;font-family:"Josefin Sans",sans-serif;font-weight:600;font-size:18px;letter-spacing:1px}
.foot-links{top:4424px;left:538px;list-style:none;font-size:15.5px;line-height:27.6px;color:#444}
.contact-row{position:absolute;left:758px;display:flex;gap:10px;font-size:15.5px;line-height:27px;color:#444}
.contact-row svg{margin-top:6px;flex:none}
.rule{top:4663px;left:111px;width:976px;height:1px;background:var(--line)}
.legal{top:4702px;left:111px;font-size:15px;color:#444}
.social{position:absolute;top:4692px;width:38px;height:38px;border-radius:50%;border:1.5px solid var(--violet)}
</style>
</head>
<body>

<section class="hero abs" role="img" aria-label="Photo of a city skyline at sunset under a purple sky"></section>
<div class="topbar abs">
  <span>&#9742; 1 800 555 0142</span><span class="sep">|</span>
  <span>&#9993; info@wellspringcrest.org</span><span class="sep">|</span>
  <span>Patient Portal</span>
  <span class="donate">DONATE</span>
</div>
<nav class="nav abs">
  <div class="brand"><span class="dot"></span>Wellspring Crest</div>
  <div class="menu"><span class="active">Home</span><span>About</span><span>Services</span><span>News</span><span>Team</span><span>FAQs</span><span>Contact</span></div>
</nav>
<h1 class="hero-title abs heading">STI/STD Medical Clinic</h1>
<p class="hero-sub abs">Wellspring Crest Partners</p>
<a class="hero-btn abs">BOOK AN APPOINTMENT</a>

<div class="welcome-art abs" role="img" aria-label="Soft illustration of a smiling patient with colourful ribbon graphics"></div>
<h2 class="welcome-title abs heading">Welcome to<br>Wellspring Crest<br>Partners</h2>
<p class="welcome-copy abs body-copy">Lorem ipsum dolor sit amet, consectetur adipiscinglit, sed do eiusmod tempor incididunt ut labore et dolore magna aliqua. Ut enim ad minim veniam, quis nostud exercitation ullamco laboris nisi ut aliquip ex ea colido consequat. Duis aute irure dolor in reprehenderit invol uptate velit esse cillum dolore eu fugiat nulla pariaturl excepteur sint occaecat cupidatat.</p>
<a class="btn-outline" style="top:1252px;left:645px;width:157px;height:51px">READ MORE</a>

<section class="treatments abs"></section>
<h2 class="section-title abs heading" style="top:1500px">Treatments</h2>

<div class="treat" style="left:119px">
  <svg width="182" height="182" viewBox="0 0 182 182"><circle cx="91" cy="91" r="89" fill="none" stroke="#2f5fbf" stroke-width="3"/><circle cx="91" cy="91" r="80" fill="#2f5fbf"/><circle cx="91" cy="91" r="20" fill="none" stroke="#fff" stroke-width="5"/><g stroke="#fff" stroke-width="5" stroke-linecap="round"><line x1="91" y1="50" x2="91" y2="66"/><line x1="91" y1="116" x2="91" y2="132"/><line x1="50" y1="91" x2="66" y2="91"/><line x1="116" y1="91" x2="132" y2="91"/><line x1="62" y1="62" x2="73" y2="73"/><line x1="109" y1="109" x2="120" y2="120"/><line x1="120" y1="62" x2="109" y2="73"/><line x1="73" y1="109" x2="62" y2="120"/></g></svg>
  <h3>Chlamydia</h3>
  <p>Nemo enim ipsam volu ptatem quia voluptas sit asp ernatur aut odit aut fugit sed quiama conse.</p>
</div>
<div class="treat" style="left:367px">
  <svg width="182" height="182" viewBox="0 0 182 182"><circle cx="91" cy="91" r="89" fill="none" stroke="#6a3fb0" stroke-width="3"/><circle cx="91" cy="91" r="80" fill="#6a3fb0"/><path d="M91 52c-14 0-18 16-10 30L62 128l10 6 19-38 19 38 10-6-19-46c8-14 4-30-10-30z" fill="none" stroke="#fff" stroke-width="5" stroke-linejoin="round"/></svg>
  <h3>HIV Medical Care</h3>
  <p>Nemo enim ipsam volu ptatem quia voluptas sit asp ernatur aut odit aut fugit sed quiama conse.</p>
</div>
<div class="treat" style="left:616px">
  <svg width="182" height="182" viewBox="0 0 182 182"><circle cx="91" cy="91" r="89" fill="none" stroke="#b0479f" stroke-width="3"/><circle cx="91" cy="91" r="80" fill="#b0479f"/><path d="M52 70c10-12 56-14 76-8 6 10-4 26-30 38-16 8-28 24-34 14-8-14-20-28-12-44z" fill="none" stroke="#fff" stroke-width="5" stroke-linejoin="round"/><line x1="92" y1="100" x2="92" y2="128" stroke="#fff" stroke-width="5" stroke-linecap="round"/></svg>
  <h3>Hepatitis A B C</h3>
  <p>Nemo enim ipsam volu ptatem quia voluptas sit asp ernatur aut odit aut fugit sed quiama conse.</p>
</div>
<div class="treat" style="left:866px">
  <svg width="182" height="182" viewBox="0 0 182 182"><circle cx="91" cy="91" r="89" fill="none" stroke="#ee5a3c" stroke-width="3"/><circle cx="91" cy="91" r="80" fill="#ee5a3c"/><path d="M91 50l32 12v26c0 22-14 36-32 44-18-8-32-22-32-44V62z" fill="none" stroke="#fff" stroke-width="5" stroke-linejoin="round"/><circle cx="91" cy="90" r="15" fill="none" stroke="#fff" stroke-width="4"/><path d="M91 82v16M83 90h16" stroke="#fff" stroke-width="4" stroke-linecap="round"/></svg>
  <h3>PrEP</h3>
  <p>Nemo enim ipsam volu ptatem quia voluptas sit asp ernatur aut odit aut fugit sed quiama conse.</p>
</div>
<a class="btn-outline" style="top:1984px;left:521px;width:158px;height:52px">VIEW MORE</a>

<section class="std abs"></section>
<h2 class="std-title abs heading">Sexually Transmitted<br>Diseases &amp; Infections<br>(STDs &amp; STIs)</h2>
<p class="std-copy abs body-copy" style="color:#eceaff">Lorem ipsum dolor sit amet, consectetur adipiscinglit, sed do eiusmod tempor incididunt ut labore et dolore magna aliqua. Ut enim ad minim veniam, quis nostud exercitation ullamco laboris nisi ut aliquip ex ea colido consequat. Duis aute irure dolor in reprehenderit invol uptate velit esse cillum dolore eu fugiat nulla pariaturl excepteur sint occaecat cupidatat.</p>
<a class="btn-outline btn-light" style="top:2598px;left:111px;width:159px;height:52px">READ MORE</a>
<a class="pill" style="top:2198px">Symptoms and Causes</a>
<a class="pill" style="top:2292px">Management and Treatment</a>
<a class="pill" style="top:2387px">Diagnosis and Tests</a>
<a class="pill" style="top:2481px">Prevention</a>

<h2 class="section-title abs heading" style="top:2808px">Become a Member</h2>
<div class="member-photo abs" role="img" aria-label="Photo of a smiling diverse group of people in matching light blue t-shirts"></div>
<p class="member-text abs">Join our community to find support and connect to other women living with STI/STD.</p>
<a class="btn-outline" style="top:3361px;left:521px;width:158px;height:50px">JOIN NOW</a>

<section class="appt abs"></section>
<h2 class="section-title appt-title abs heading">Book an Appointment</h2>
<p class="appt-sub abs">Fill out the form to make an appointment</p>
<span class="label" style="top:3636px;left:165px">First Name</span>
<span class="label" style="top:3636px;left:606px">Last Name</span>
<div class="field" style="top:3674px;left:165px;width:427px;height:52px"></div>
<div class="field" style="top:3674px;left:606px;width:428px;height:52px"></div>
<span class="label" style="top:3745px;left:165px">Email</span>
<span class="label" style="top:3745px;left:606px">Phone</span>
<div class="field" style="top:3781px;left:165px;width:427px;height:52px"></div>
<div class="field" style="top:3781px;left:606px;width:428px;height:52px"></div>
<span class="label" style="top:3855px;left:165px">What is your location preference?</span>
<span class="label" style="top:3855px;left:606px">What is your appointment preference?</span>
<div class="field" style="top:3892px;left:165px;width:427px;height:52px"></div>
<label class="check" style="left:608px"><span class="box"></span>In-Person</label>
<label class="check" style="left:728px"><span class="box"></span>Telehealth</label>
<span class="label" style="top:3966px;left:165px">What are you inquiring about?</span>
<div class="field" style="top:4003px;left:165px;width:869px;height:139px"></div>
<a class="btn-outline btn-light" style="top:4184px;left:538px;width:122px;height:50px;font-size:16px">SUBMIT</a>

<div class="brand abs" style="top:4410px;left:111px;font-size:30px"><span class="dot" style="width:46px;height:46px"></span>Wellspring Crest</div>
<p class="footer-copy abs">Neque porro qucui dolorem ips um quia do lor sit amet, consectetur, adipisci velit, sed quia non numquam eius modi tempora inc iduneque porro quisqua.</p>

<h4 class="foot-head" style="left:536px">QUICK LINKS</h4>
<ul class="foot-links abs"><li>Home</li><li>About</li><li>Services</li><li>News</li><li>Team</li><li>FAQs</li><li>Contact</li></ul>

<h4 class="foot-head" style="left:756px">CONTACT US</h4>
<div class="contact-row" style="top:4424px"><svg width="11" height="15" viewBox="0 0 11 15"><path d="M5.5 0A5.5 5.5 0 0 0 0 5.5C0 9.5 5.5 15 5.5 15S11 9.5 11 5.5A5.5 5.5 0 0 0 5.5 0zm0 7.5a2 2 0 1 1 0-4 2 2 0 0 1 0 4z" fill="#5a2ea6"/></svg><span>2400 Cypress Lane, Suite 120<br>Lakeview, FL 32010</span></div>
<div class="contact-row" style="top:4505px"><svg width="13" height="13" viewBox="0 0 13 13"><path d="M3 0l2 3-1.5 1.5a8 8 0 0 0 5 5L10 8l3 2-1.5 3C6 13 0 7 0 1.5z" fill="#5a2ea6"/></svg><span>1 800 555 0142</span></div>
<div class="contact-row" style="top:4561px"><svg width="14" height="11" viewBox="0 0 14 11"><rect width="14" height="11" rx="1" fill="#5a2ea6"/><path d="M1 1l6 5 6-5" fill="none" stroke="#fff" stroke-width="1.3"/></svg><span>info@wellspringcrest.org</span></div>

<div class="rule abs"></div>
<p class="legal abs">©2022, Wellspring Crest Partners. All rights reserved.</p>
<span class="social" style="left:955px" aria-label="Social link"></span>
<span class="social" style="left:1002px" aria-label="Social link"></span>
<span class="social" style="left:1049px" aria-label="Social link"></span>

</body>
</html>
```